Label Design Brief - Quillmere Health
Label Panel Dimensions 1.25" W x 2.375" H (front/back panel)
Hello - our company develops novel products for the skin, & hair care industry as well as dietary supplements. We're looking for a label design for a new product. The product is a premium Topical hair loss/growth serum. I attached the brand logo & 2 other sister products along with some competitive products.
The product is a topical natural hair loss serum for men & women to regrow new hair and help restore hair loss & thinning hair due to vitamin deficiencies, hormone imbalance & aging. It is a science based efficacious serum with a century’s old medicinal herbal formula.
Attached is our logo & some files of other competition. The label must have an upscale, technology flair to it. The product is clinically effective, leveraged by Ancient Wisdom and Modern Science.
Below are attached files of 2 of our products & other generic competition for your perusal.

https://www.shopvarnel.example/item/K7T2QPL4XR?src=listing_offer

https://www.shopvarnel.example/item/K7T5MDR9WA/src=alt-list-view?vw=1&src=listing_lowcost

Target Market(s)

men & women age 18-80

Requirements
Must have
• see brief
Should not have
• Please do not have a picture of a man or a women on the label.

```html
<!DOCTYPE html>
<html lang="en">
<head>
<meta charset="UTF-8">
<title>Quillmere Health – DHT Blocker Label</title>
<link href="https://fonts.googleapis.com/css2?family=Open+Sans:wght@400;600;700;800&display=swap" rel="stylesheet">
<style>
  :root {
    --page-bg: #f2f2f2;
    --label-bg: #ffffff;
    --ink: #111111;
    --brand-brown: #8a5a3c;
    --band-black: #0d0d0d;
    --accent-orange: #e8843a;
    --silver-dark: #8c8c8c;
    --silver-light: #f4f4f4;
    --rule: #1a1a1a;
    --stone-light: #eeeeee;
    --stone-dark: #bdbdbd;
  }
  * { margin: 0; padding: 0; box-sizing: border-box; }
  html, body {
    width: 1200px; height: 1200px; overflow: hidden;
    background: var(--page-bg);
    font-family: "Open Sans", Arial, sans-serif;
    color: var(--ink);
  }
  .label {
    position: absolute;
    left: 340px; top: 67px;
    width: 520px; height: 1066px;
    background: var(--label-bg);
    box-shadow: 0 2px 10px rgba(0,0,0,0.08);
  }
  .brand {
    position: absolute; top: 142px; left: 0; width: 100%;
    text-align: center; line-height: 1;
    font-size: 40px; font-weight: 400; letter-spacing: 1px;
    color: var(--brand-brown);
  }
  .claim-band {
    position: absolute; top: 291px; left: 0; width: 100%; height: 86px;
    background: var(--band-black);
    display: flex; align-items: center; justify-content: center;
    color: var(--accent-orange);
    font-size: 42px; font-weight: 700; letter-spacing: 0.5px;
  }
  .product-name { font-weight: 800; color: var(--ink); }
  .product-name .dht,
  .product-name .blocker {
    position: absolute; left: 0; width: 100%;
    text-align: center; line-height: 1;
  }
  .product-name .dht { top: 379px; font-size: 165px; letter-spacing: -2px; }
  .product-name .blocker { top: 548px; font-size: 70px; letter-spacing: -1px; }
  .audience-band {
    position: absolute; top: 647px; left: 56px; width: 410px; height: 53px;
    background: linear-gradient(90deg, var(--silver-dark) 0%, var(--silver-light) 55%, var(--silver-dark) 100%);
    display: flex; align-items: center; padding-left: 22px;
    font-size: 27px; font-weight: 600; color: var(--ink);
  }
  .features {
    position: absolute; top: 785px; left: 46px;
    list-style: none;
    font-size: 27px; font-weight: 600; line-height: 36px;
  }
  .features li::before {
    content: ""; display: inline-block;
    width: 9px; height: 9px; background: var(--ink);
    margin-right: 10px; vertical-align: middle;
  }
  .feature-rule {
    position: absolute; top: 877px; left: 46px;
    width: 280px; height: 3px; background: var(--rule);
  }
  .herb-illustration {
    position: absolute; top: 767px; left: 328px;
    width: 163px; height: 160px;
    border-radius: 10px 10px 50% 50%;
    background: radial-gradient(ellipse at 40% 40%, var(--stone-light), var(--stone-dark));
  }
  .volume {
    position: absolute; top: 996px; left: 0; width: 100%;
    text-align: center; line-height: 1; font-size: 24px; font-weight: 600;
  }
</style>
</head>
<body>
  <main class="label">
    <div class="brand">Quillmere Health</div>
    <div class="claim-band">GROWTH ACTIVATOR</div>
    <h1 class="product-name">
      <span class="dht">DHT</span>
      <span class="blocker">BLOCKER</span>
    </h1>
    <div class="audience-band">For Men and Women</div>
    <ul class="features">
      <li>Paraben Free</li>
      <li>Time-Released</li>
    </ul>
    <div class="feature-rule"></div>
    <div class="herb-illustration" role="img" aria-label="White mortar and pestle illustration"></div>
    <div class="volume">2 fl.oz</div>
  </main>
</body>
</html>
```